Covid 19 Exit Strategy one page brochure

I would like to design, and will need URGENT help, a brochure detailing a Covid 19 Exit Strategy plan. This brochure will need to be understood easily and the graphics inside should make it easy for people to understand without reading the entire text. This project is quite urgent and needs to be completed THIS WEEK - by Saturday may 16th at the latest. I am attaching two examples. I will provide the text.

```html
<!DOCTYPE html>
<html lang="en">
<head>
<meta charset="utf-8">
<title>Covid-19 Phased Exit Strategy</title>
<link href="https://fonts.googleapis.com/css2?family=Montserrat:wght@400;800;900&family=Roboto:wght@400;700&display=swap" rel="stylesheet">
<style>
:root{
  --bg:#ffffff;
  --shadow:#dedede;
  --page:#f7f7f8;
  --ink:#2b2b2b;
  --blue:#1f7fd0;
  --teal:#1eb3c7;
  --navy:#14336a;
  --row-alt:#efefef;
  --frame:#55585c;
}
*{box-sizing:border-box;margin:0;padding:0}
html,body{width:1200px;height:2231px;overflow:hidden;background:var(--bg)}
body{position:relative;font-family:'Roboto',Arial,sans-serif;color:var(--ink)}
.sheet-shadow{position:absolute;width:487px;height:630px;background:var(--shadow)}
.page{position:absolute;width:487px;height:630px;background:var(--page);overflow:hidden}
.virus-top{position:absolute;left:0;top:0;width:100%;height:190px;
  background:radial-gradient(circle at 62% 20%,#4d86e6 0 18%,transparent 19%),
  radial-gradient(circle at 33% 45%,#3f78df 0 11%,transparent 12%),
  radial-gradient(circle at 88% 60%,#a9c8f3 0 14%,transparent 15%),
  linear-gradient(180deg,#cfe0f8 0%,#eef3fb 70%,rgba(247,247,248,0) 100%)}
.virus-bottom{position:absolute;left:0;bottom:0;width:100%;height:118px;
  background:radial-gradient(circle at 20% 90%,#1a9db8 0 16%,transparent 17%),
  radial-gradient(circle at 70% 95%,#1f8fb0 0 18%,transparent 19%),
  radial-gradient(circle at 95% 70%,#25b1c4 0 12%,transparent 13%),
  linear-gradient(0deg,#2aa9c4 0%,#8fd3df 45%,rgba(247,247,248,0) 100%)}
.cover-frame{position:absolute;inset:13px 13px;border:1.5px solid var(--frame)}
.title-box{position:absolute;border:1.5px solid var(--frame);text-align:center;background:rgba(255,255,255,.6)}
.title-main{font-family:'Montserrat',sans-serif;font-weight:900;
  background:linear-gradient(90deg,var(--blue),var(--teal));-webkit-background-clip:text;background-clip:text;color:transparent;line-height:1}
.title-sub{font-family:'Montserrat',sans-serif;font-weight:800;color:var(--blue);letter-spacing:.04em;line-height:1.1}
.cover .title-box{left:70px;top:227px;width:346px;height:115px;padding-top:14px}
.cover .title-main{font-size:48px}
.cover .title-sub{font-size:21px;margin-top:6px}
.credit{position:absolute;left:50%;bottom:-9px;transform:translateX(-50%);background:#f7f7f8;padding:0 6px;
  font-family:'Montserrat',sans-serif;font-size:16px;white-space:nowrap;color:#333}
.cover-intro{position:absolute;left:48px;top:372px;width:390px;font-family:'Montserrat',sans-serif;font-size:9.4px;line-height:1.22;text-align:justify;text-align-last:center;color:#333}

.req-page{background:linear-gradient(180deg,#8fb4ee 0%,#d6e4f8 30%,#e7f1f5 70%,#47b7c9 100%)}
.req-card{position:absolute;left:29px;top:30px;width:433px;height:569px;background:#fff;box-shadow:0 0 4px rgba(0,0,0,.25)}
.req-head{height:79px;background:linear-gradient(180deg,var(--navy),var(--teal));color:#fff;text-align:center;
  font-family:'Montserrat',sans-serif;font-weight:800;font-size:25px;line-height:1.05;padding-top:19px}
.req-row{height:54.4px;display:flex;align-items:center;gap:16px;padding:0 40px 0 30px;font-size:7px;line-height:1.25}
.req-row:nth-child(odd){background:var(--row-alt)}
.req-row.right{flex-direction:row-reverse;text-align:right;padding:0 38px 0 32px}
.req-row p{flex:1}
.icon{flex:none;width:32px;height:32px;border-radius:6px;background:linear-gradient(135deg,#8fb0e8,#e07a6a)}
.icon.sm{width:22px;height:22px;border-radius:5px}

.stage .title-box{left:126px;top:20px;width:240px;height:74px;padding-top:8px}
.stage .title-main{font-size:29px}
.stage .title-sub{font-size:14px;margin-top:3px}
.stage-tag{position:absolute;left:50%;bottom:-7px;transform:translateX(-50%);background:var(--blue);color:#fff;
  font-family:'Montserrat',sans-serif;font-weight:800;font-size:11px;padding:1px 7px;letter-spacing:.04em}
.stage-intro{position:absolute;left:52px;right:40px;top:110px;text-align:center;font-size:6.3px;font-weight:700;line-height:1.28}
.col{position:absolute;display:flex;flex-direction:column;gap:12px}
.item{display:flex;gap:8px;align-items:flex-start;font-size:6.6px;line-height:1.3}
.item p{flex:1}
.s1 .col.left{left:26px;top:152px;width:196px}
.s1 .col.right{left:244px;top:152px;width:226px}
.s23 .col.left{left:36px;top:177px;width:196px}
.s23 .col.right{left:258px;top:177px;width:194px}
</style>
</head>
<body>

<div class="sheet-shadow" style="left:371px;top:106px"></div>
<section class="page cover" style="left:403px;top:87px">
  <div class="virus-top" role="img" aria-label="Blue coronavirus particle illustration"></div>
  <div class="virus-bottom" role="img" aria-label="Teal coronavirus particle illustration"></div>
  <div class="cover-frame"></div>
  <div class="title-box">
    <div class="title-main">COVID-19</div>
    <div class="title-sub">PHASED EXIT STRATEGY</div>
    <div class="credit">Developed by Dana Whitlock</div>
  </div>
  <p class="cover-intro">Pandemics have, historically, seen their end both medically - via herd immunity or immunizations. And while there are several clinical trials underway for potential Covid-19 vaccines, we are still a long way from deploying an effective vaccine and one that will stand the test of time as the virus changes. Covid-19 pandemic will be considered ‘ended’ when there are only occasional traces of localized cases that are quickly contained in specific locations., Today and in the absence of an effective vaccine(s) and for the re-opening of the economies and social activities to be successful, it is critical that the following basic conditions be in place before any lockdowns are lifted and before social activities resume.</p>
</section>

<div class="sheet-shadow" style="left:65px;top:818px"></div>
<section class="page req-page" style="left:97px;top:800px" role="img" aria-label="Coronavirus particle background">
  <div class="req-card">
    <div class="req-head">GENERAL<br>REQUIREMENTS</div>
    <div class="req-row"><div class="icon" role="img" aria-label="Report icon"></div><p>Single digit downward trend of documented cases within the past 14-days.</p></div>
    <div class="req-row right"><div class="icon" role="img" aria-label="Patient and shield icon"></div><p>Hospitals and the health care system are capable of treating patients without operating on a crisis mode.</p></div>
    <div class="req-row"><div class="icon" role="img" aria-label="Microscope icon"></div><p>Ability to screen and test symptomatic individuals within 24 hours of identification. Increased and sufficient testing capacity, to test at least 50% of all population if necessary within a timeframe of 3 months.</p></div>
    <div class="req-row right"><div class="icon" role="img" aria-label="ICU bed icon"></div><p>Ability to surge ICU capacity on a short notice - 24h.</p></div>
    <div class="req-row"><div class="icon" role="img" aria-label="Magnifier icon"></div><p>Ability to track and trace infected patients and contacts on a live basis and across the country and ability to react quickly to any unusual trends or outbreaks.</p></div>
    <div class="req-row right"><div class="icon" role="img" aria-label="Target icon"></div><p>Plan in place to trigger targeted or full-scale containment in case of sudden outbreaks</p></div>
    <div class="req-row"><div class="icon" role="img" aria-label="Face mask icon"></div><p>Mandatory use of masks (at least surgical grade) for everyone in all public areas and at work. Mandatory use of N95, or equivalent, masks for all healthcare front workers and for all government agencies and authorities that are involved in overseeing the containment activities.</p></div>
    <div class="req-row right"><div class="icon" role="img" aria-label="Temperature check icon"></div><p>Mandatory daily checks of body temperature for everyone at the workplace or entering public areas.</p></div>
    <div class="req-row"><div class="icon" role="img" aria-label="Hand sanitizer icon"></div><p>Mandatory sanitation in all places - use of disinfection available on a large scale.</p></div>
  </div>
</section>

<div class="sheet-shadow" style="left:610px;top:818px"></div>
<section class="page stage s1" style="left:642px;top:800px">
  <div class="virus-bottom" role="img" aria-label="Teal coronavirus particle illustration"></div>
  <div class="title-box"><div class="title-main">COVID-19</div><div class="title-sub">PHASED EXIT STRATEGY</div><div class="stage-tag">STAGE 1</div></div>
  <p class="stage-intro">To enter this stage, additional to the general requirements, the Effective Reproduction Number (Rt) must be less than 1 and the death rate at less than 3%.<br>The economy and social activities can resume in this sequence:</p>
  <div class="col left">
    <div class="item"><div class="icon sm" role="img" aria-label="Elderly person icon"></div><p>Elderly (60+ years old) and vulnerable individuals should continue to self-isolate.</p></div>
    <div class="item"><div class="icon sm" role="img" aria-label="Home office icon"></div><p>Work from home should continue whenever and as much as possible.</p></div>
    <div class="item"><div class="icon sm" role="img" aria-label="Bus icon"></div><p>Non-essential travel should be minimized between cities and regions (and within cities and regions where covid-19 infections are still a risk)</p></div>
    <div class="item"><div class="icon sm" role="img" aria-label="Small group icon"></div><p>Small businesses (300 people and less) can reopen as well with the same conditions as large businesses.</p></div>
    <div class="item"><div class="icon sm" role="img" aria-label="Pharmacy icon"></div><p>Pharmacies will continue to be open. However, they must make available disinfectant for use by clients and will continue to comply with social distancing. Pharmacies should limit the number of client/patient in their stores not to exceed 30% of the standard capacity.</p></div>
    <div class="item"><div class="icon sm" role="img" aria-label="Praying hands icon"></div><p>Religious sites can reopen with a maximum capacity of 30% or less. Social distancing and wearing masks is mandatory. Religious sites should organize (volunteers can help) to check body temperature of everyone accessing the site and provide disinfectant at entry.</p></div>
    <div class="item"><div class="icon sm" role="img" aria-label="Coffee shop icon"></div><p>Coffee &amp; restaurants can reopen but must operate at 30% capacity as well and comply with social distancing. Clients must wear as much as possible their masks if they are not consuming food/coffee. Clients should avoid to talking to each other with masks off.</p></div>
    <div class="item"><div class="icon sm" role="img" aria-label="Events icon"></div><p>Large scale events (cinema, theaters, sport, business conferences, etc.) should remain closed or operate virtually. Sport events can resume but without spectators. Athletes and the staff surrounding them should be tested, disinfectants should be available and masks used as much as reasonably possible.</p></div>
  </div>
  <div class="col right">
    <div class="item"><div class="icon sm" role="img" aria-label="Group limit icon"></div><p>No more than 5 people maximum gathering at a time in public areas and at work.</p></div>
    <div class="item"><div class="icon sm" role="img" aria-label="Distancing icon"></div><p>Social distancing should continue to be re-enforced in public areas, atwork and in all areas reopened.</p></div>
    <div class="item"><div class="icon sm" role="img" aria-label="Office worker icon"></div><p>Large businesses (300 people and more, manufacturing, services, etc.) can reopen progressively. Common areas should remain closed (cafeteria, restaurant, gym, meeting rooms of no more than 5 people).</p></div>
    <div class="item"><div class="icon sm" role="img" aria-label="Shop icon"></div><p>Commercial shops can reopen. Shops should control the flow of people in their facilities not to exceed 30% at a time of standard capacity. Shops should provide disinfectant and temperature control at entry.</p></div>
    <div class="item"><div class="icon sm" role="img" aria-label="Car icon"></div><p>Transportation (buses, taxis, airlines) will resume progressively. No air travels permitted in and out of Covid-19 known hotspots, locally or internationally. Entry to country should be limited and strictly controlled. All landing passengers and visitors regardless of the country of origin should be tested for Covid-19 at arrival. All passengers and visitors will undergo a temperature check at arrival. No more than 3 people at a time in a taxi/ride-share including the driver. All passengers wearing masks. Buses should operate with no more than 30% customer's capacity per bus.</p></div>
    <div class="item"><div class="icon sm" role="img" aria-label="Hotel icon"></div><p>Hotels &amp; tourism (museums, etc.) can reopen but must operate at 30% or less capacity. All common areas (restaurants, gyms, swimming pools, conference rooms, etc.) should remain closed.</p></div>
    <div class="item"><div class="icon sm" role="img" aria-label="School icon"></div><p>All schools should remain closed. On-line courses should continue be the preferred method for education</p></div>
  </div>
</section>

<div class="sheet-shadow" style="left:65px;top:1517px"></div>
<section class="page stage s23" style="left:97px;top:1499px">
  <div class="virus-bottom" role="img" aria-label="Teal coronavirus particle illustration"></div>
  <div class="title-box"><div class="title-main">COVID-19</div><div class="title-sub">PHASED EXIT STRATEGY</div><div class="stage-tag">STAGE 2</div></div>
  <p class="stage-intro">To enter stage 2 of the Covid-19 Exit Strategy, compliance to the general requirements is compulsory, additional to a successful Stage 1 outcome.The Effective Reproduction Number (Rt) for Stage 2 must be less than 0.5 and the death rate stabilized at less than 1.5%.<br><br>The economy and social activities can resume in this sequence:</p>
  <div class="col left">
    <div class="item"><div class="icon sm" role="img" aria-label="Elderly person icon"></div><p>Elderly (60+ years old) and vulnerable individuals should continue to self-isolate as much as possible.</p></div>
    <div class="item"><div class="icon sm" role="img" aria-label="Home office icon"></div><p>Work from home should if possible or for jobs that do not have to be necessarily in an office setup.</p></div>
    <div class="item"><div class="icon sm" role="img" aria-label="Bus icon"></div><p>Travel can resume between cities and regions. The same containment restrictions should apply to any existing hotspot.</p></div>
    <div class="item"><div class="icon sm" role="img" aria-label="Large group icon"></div><p>Large businesses (300 people and more, manufacturing, services, etc.) will continue to operate. Common areas should open but social distancing should remain (cafeteria, restaurant, gym, meeting rooms of no more than 10 people).</p></div>
    <div class="item"><div class="icon sm" role="img" aria-label="Pharmacy icon"></div><p>Pharmacies will continue to be open and will need to operate a 50% capacity</p></div>
    <div class="item"><div class="icon sm" role="img" aria-label="Praying hands icon"></div><p>Religious sites can operate with a maximum capacity of 50%. Social distancing and wearing masks should be enforced. Sites should continue to check body temperature of everyone accessing the site and provide disinfectant at entry.</p></div>
    <div class="item"><div class="icon sm" role="img" aria-label="Coffee shop icon"></div><p>Coffee &amp; restaurants can operate at 50% capacity and continue comply with social distancing. Clients must wear as much as possible their masks if they are not consuming food/coffee.</p></div>
    <div class="item"><div class="icon sm" role="img" aria-label="School icon"></div><p>Schools can reopen in parallel with on-line education. Social distancing and re-arranging school seating to prevent the spread of infection is mandatory</p></div>
    <div class="item"><div class="icon sm" role="img" aria-label="Events icon"></div><p>Large scale events (cinema, theaters, sport, business conferences, etc.) could resume under strict social distancing. People should wear masks.</p></div>
  </div>
  <div class="col right">
    <div class="item"><div class="icon sm" role="img" aria-label="Group limit icon"></div><p>No more than 10 people maximum gathering at a time in public areas and at work.</p></div>
    <div class="item"><div class="icon sm" role="img" aria-label="Distancing icon"></div><p>Social distancing can be relaxed. However people should continue to wear masks and use disinfectants.</p></div>
    <div class="item"><div class="icon sm" role="img" aria-label="Surgeon icon"></div><p>Elective surgeries can resume in hospitals and clinics that are equipped to comply with all general requirements.</p></div>
    <div class="item"><div class="icon sm" role="img" aria-label="Small group icon"></div><p>Small businesses (300 people and less) will continue to operate with the same conditions as large businesses.</p></div>
    <div class="item"><div class="icon sm" role="img" aria-label="Car icon"></div><p>Transportation (buses, taxis, and airlines) will continue to operate. Still no air travels permitted in and out of Covid-19 known hotspots, locally or internationally. Entry to country should be relaxed but remain controlled. Airports should continue to use thermo cameras to monitor passenger's temperature at landing. Airports should be equipped to test for Covid-19 if necessary. Transportation by taxi/ride-share continues, however, passengers wear masks. Buses could operate with 50% capacity per bus.</p></div>
    <div class="item"><div class="icon sm" role="img" aria-label="Hotel icon"></div><p>Hotels &amp; tourism (museums, etc.) can operate at 50% capacity. All common areas (restaurants, gyms, swimming pools, conference rooms, etc.) could reopen. Gatherings are limited to 10 people or less and can be expanded with social distancing and wearing protective masks.</p></div>
  </div>
</section>

<div class="sheet-shadow" style="left:610px;top:1517px"></div>
<section class="page stage s23" style="left:642px;top:1499px">
  <div class="virus-bottom" role="img" aria-label="Teal coronavirus particle illustration"></div>
  <div class="title-box"><div class="title-main">COVID-19</div><div class="title-sub">PHASED EXIT STRATEGY</div><div class="stage-tag">STAGE 3</div></div>
  <p class="stage-intro">To enter stage 3 of the Covid-19 Exit Strategy, compliance to the general requirements is compulsory, additional to a successful Stage 2 outcome. The Effective Reproduction Number (Rt) for Stage 3 must be less than 0.3 and the death rate stabilized at less than 1%.<br><br>The economy and social activities can resume in this sequence:</p>
  <div class="col left">
    <div class="item"><div class="icon sm" role="img" aria-label="Elderly person icon"></div><p>Elderly (60+ years old) and vulnerable individuals may resume all previously exercised activities without restrictions.</p></div>
    <div class="item"><div class="icon sm" role="img" aria-label="Bus icon"></div><p>Travel can resume between cities and regions and out of country travel. The same containment restrictions as Stage 1 and 2 would continue to apply to any existing hotspot.</p></div>
    <div class="item"><div class="icon sm" role="img" aria-label="Large group icon"></div><p>Large businesses (300 people and more, manufacturing, services, etc.) will resume normal business practices. Wear of masks is recommended but not mandatory.</p></div>
    <div class="item"><div class="icon sm" role="img" aria-label="Shop icon"></div><p>Commercial shops can operate on a normal mode - previous to covid- 19. Wear of masks could be recommended in certain areas.</p></div>
    <div class="item"><div class="icon sm" role="img" aria-label="Car icon"></div><p>Transportation (buses, taxis, and airlines) will operate at a normal capacity. Still no air travels permitted in and out of Covid-19 known hotspots, locally or internationally. Entry to country should be relaxed and operate normally. Airports should continue to use thermo cameras to monitor passenger's temperature at landing. Airports should be equipped to test for Covid-19 if necessary. Transportation by taxi/ride-share and buses will resume on a normal mode. Wear of masks is elective.</p></div>
    <div class="item"><div class="icon sm" role="img" aria-label="Events icon"></div><p>Large scale events (cinema, theaters, sport, business conferences, etc.) could resume under moderate social distancing. People may elect to wear masks.</p></div>
  </div>
  <div class="col right">
    <div class="item"><div class="icon sm" role="img" aria-label="Group icon"></div><p>Restrictions as to the number of people gathering together can benlifted. Social distancing can be relaxed. However, wear of masks may continue.</p></div>
    <div class="item"><div class="icon sm" role="img" aria-label="Surgeon icon"></div><p>All hospital and clinic surgeries can resume in hospitals in compliance with standard hospital and health care procedures.</p></div>
    <div class="item"><div class="icon sm" role="img" aria-label="Small group icon"></div><p>Small businesses (300 people and less) will operate with the same conditions as large businesses.</p></div>
    <div class="item"><div class="icon sm" role="img" aria-label="Pharmacy icon"></div><p>Pharmacies can operate at a normal state.</p></div>
    <div class="item"><div class="icon sm" role="img" aria-label="Praying hands icon"></div><p>Religious sites can operate normally. Wear of masks should be elective.</p></div>
    <div class="item"><div class="icon sm" role="img" aria-label="Hotel icon"></div><p>Hotels &amp; tourism (museums, etc.) can operate at 100% capacity including all common areas</p></div>
    <div class="item"><div class="icon sm" role="img" aria-label="Coffee shop icon"></div><p>Coffee &amp; restaurants can resume normal operations. Clients may wear masks for personal protection if they wish to.</p></div>
    <div class="item"><div class="icon sm" role="img" aria-label="School icon"></div><p>Schools can resume operations. Re-arranging school seating should continue until a vaccine is found.</p></div>
  </div>
</section>

</body>
</html>
```